Homes, Invest in Non-performing loans

We need only 3 web pages, one for the home, one for the content, one for the properties.
The main focus of our business is to offer non performing loans (before foreclosures) to the general public. All the non-performing mortgages will end in a house, an apartment, a store, etc.
Our customers are able to invest from 10,000usd to 1,000,000usd (average 50,000usd).
Our customers' usual focus groups are employees who want second earnings, perceiving the business feeling without outlay time. They look for a solid finance sense corporation that confers them certainty.
Nearly all our clients desire the house, apartment, store, etc. more than the actual earnings.
The name of our company is BRAMLEY
Reason: We value the time and effort you already invest in our project. We realize that we did't come back on some of the doubts requested by the designers. It will be inequitable to the designers who prerequisite our feedback. We also appreciate the comprehension of the community in this postponement.
Reason: Designers,
We really apreciate all the time and effort you put on our project. From the begining we ask for 3 pages, so now we will leave the 10 finalist and provide some extra time to submit the other 2 pages.
We will race the price in 10%
Target Market(s)
Our customers average investors works as employees and want to have a second income or business without spending time. (People from 35 to 50)
Industry/Entity Type
Finance
Requirements
Should not have
- FLASH

```html
<!DOCTYPE html>
<html lang="en">
<head>
<meta charset="utf-8">
<title>BRAMLEY – Remates Hipotecarios</title>
<link rel="stylesheet" href="https://fonts.googleapis.com/css2?family=Arimo:wght@400;700&family=Archivo+Narrow:wght@400;700&family=Alegreya+Sans:wght@400;700&display=swap">
<style>
  :root {
    --olive: #9a9a1c;
    --olive-dark: #75750e;
    --olive-light: #c4c23a;
    --olive-text: #7d7a12;
    --ink: #222426;
    --body: #3a3a3a;
    --muted: #555;
    --nav-top: #8a8a8a;
    --nav-bottom: #4a4a4a;
    --page: #f4f4f4;
    --white: #ffffff;
    --sky-top: #a8d6ee;
    --sky-bottom: #f6f8f6;
    --grass: #5cae2a;
    --grass-dark: #2f7a14;
    --rule: #d8d8d8;
  }
  * { box-sizing: border-box; margin: 0; padding: 0; }
  html, body { width: 1200px; height: 927px; overflow: hidden; }
  body { position: relative; background: var(--page); font-family: "Arimo", Arial, sans-serif; }

  .header { position: absolute; inset: 0 0 auto 0; height: 157px;
    background: linear-gradient(#fafafa, #ececec); border-top: 2px solid var(--olive); }
  .account-tab { position: absolute; left: 895px; top: 0; width: 206px; height: 28px;
    background: var(--olive); clip-path: polygon(0 0,100% 0,94% 100%,6% 100%);
    display: flex; align-items: center; justify-content: center; gap: 12px;
    color: var(--white); font-family: "Archivo Narrow", sans-serif; font-size: 14px; }
  .account-tab span + span { border-left: 1px solid rgba(255,255,255,.4); padding-left: 12px; }
  .search { position: absolute; left: 915px; top: 55px; width: 166px; height: 30px;
    border: 2px solid #c8c8c8; border-radius: 15px; background: var(--white);
    font-family: "Alegreya Sans", sans-serif; font-size: 13px; color: #333;
    padding: 5px 0 0 17px; }
  .search svg { position: absolute; right: 8px; top: 5px; }

  .nav { position: absolute; left: 0; top: 117px; width: 1200px; height: 40px;
    background: linear-gradient(var(--nav-top), #6a6a6a 50%, var(--nav-bottom));
    box-shadow: 0 3px 6px rgba(0,0,0,.25); }
  .nav ul { list-style: none; position: absolute; left: 319px; top: 0; display: flex; height: 40px; }
  .nav li { height: 40px; display: flex; align-items: center; justify-content: center; padding-top: 5px;
    color: var(--white); font-family: "Archivo Narrow", sans-serif; font-size: 16px;
    border-right: 1px solid #3f3f3f; box-shadow: 1px 0 0 #8d8d8d; }
  .nav li.active { background: linear-gradient(#9a9a9a,#7a7a7a); color: #e4df4a; }

  .brand { position: absolute; left: 124px; top: 0; width: 182px; height: 168px;
    background: var(--white); clip-path: polygon(0 0,100% 0,100% 90%,50% 100%,0 90%);
    filter: drop-shadow(0 2px 3px rgba(0,0,0,.2)); z-index: 2; }
  .brand-mark { position: absolute; left: 83px; top: 40px; width: 16px; height: 16px; background: var(--olive); }
  .brand-name { position: absolute; left: 0; top: 80px; width: 182px; text-align: center; white-space: nowrap;
    font-family: "Arimo", sans-serif; font-weight: 700; font-size: 33px; line-height: 40px;
    color: #3a3a3a; letter-spacing: -1px; }
  .brand-tagline { position: absolute; left: 22px; top: 132px; width: 138px; text-align: center;
    border-top: 1px solid #555; padding-top: 3px; white-space: nowrap;
    font-size: 8.5px; line-height: 11px; letter-spacing: 1px; color: #333; }

  .hero { position: absolute; left: 0; top: 157px; width: 1200px; height: 471px;
    background: linear-gradient(var(--sky-top), #dcecf4 30%, var(--sky-bottom) 70%); overflow: hidden; }
  .hero-title { position: absolute; left: 122px; top: 43px; font-weight: 700; font-size: 40px;
    line-height: 58px; color: var(--ink); white-space: nowrap; }
  .hero-copy { position: absolute; left: 123px; top: 180px; width: 450px; white-space: nowrap;
    font-family: "Alegreya Sans", sans-serif; font-size: 17px; line-height: 21.5px; color: var(--body); }
  .hero-copy p + p { margin-top: 21.5px; }
  .hero-copy b { color: var(--olive-text); }
  .btn { display: inline-flex; align-items: center; justify-content: center; gap: 6px;
    background: linear-gradient(var(--olive-light), var(--olive) 50%, var(--olive-dark));
    color: var(--white); font-family: "Archivo Narrow", sans-serif; font-weight: 700;
    border: 1px solid #5f5f0a; border-radius: 7px; box-shadow: inset 0 1px 0 rgba(255,255,255,.5); }
  .btn-start { position: absolute; left: 123px; top: 338px; width: 182px; height: 42px; font-size: 21px; }
  .hero-photo { position: absolute; left: 565px; top: 33px; width: 555px; height: 370px;
    background: radial-gradient(ellipse at 55% 45%, #8aa3b6, #c9d7e0 60%, rgba(240,245,248,0) 75%); }
  .hero-ground { position: absolute; left: 0; top: 370px; width: 1200px; height: 101px;
    background: linear-gradient(transparent, transparent 30%, var(--grass) 55%, var(--grass-dark)); }
  .slider-dots { position: absolute; left: 1030px; top: 383px; display: flex; gap: 9px; }
  .slider-dots i { width: 18px; height: 18px; border-radius: 50%; background: #222; display: block; }
  .slider-dots i.on { background: var(--olive); }

  .features { position: absolute; left: 123px; top: 675px; display: flex; }
  .feature { width: 246px; height: 206px; border-left: 1px solid var(--rule); position: relative; }
  .feature:last-child { border-right: 1px solid var(--rule); width: 244px; }
  .feature-head { display: flex; align-items: center; gap: 8px; padding-left: 20px; height: 56px; }
  .feature-title { font-family: "Archivo Narrow", sans-serif; font-weight: 700; font-size: 18px; color: var(--ink); white-space: nowrap; }
  .feature p { margin: 14px 0 0 33px; width: 200px; font-size: 13px; line-height: 20px; color: var(--muted); white-space: nowrap; }
  .btn-more { position: absolute; left: 112px; top: 179px; width: 100px; height: 28px; font-size: 14px; font-weight: 700; }
</style>
</head>
<body>
  <header class="header">
    <div class="account-tab"><span>&#9632; REGISTER</span><span>LOGIN</span></div>
    <div class="search">Enter keywords..
      <svg width="20" height="20" viewBox="0 0 20 20"><circle cx="8" cy="8" r="6" fill="none" stroke="#999" stroke-width="3"/><line x1="12" y1="12" x2="18" y2="18" stroke="#999" stroke-width="3"/></svg>
    </div>
  </header>

  <div class="brand">
    <span class="brand-mark"></span>
    <div class="brand-name">BRAMLEY</div>
    <div class="brand-tagline">REMATES HIPOTECARIOS</div>
  </div>

  <nav class="nav">
    <ul>
      <li class="active" style="width:88px">HOME</li>
      <li style="width:115px">ABOUT US</li>
      <li style="width:118px">SERVICES</li>
      <li style="width:153px">HOW IT WORKS</li>
      <li style="width:88px">NEWS</li>
      <li style="width:89px">BLOG</li>
      <li style="width:125px;border-right:0;box-shadow:none">CONTACT US</li>
    </ul>
  </nav>

  <section class="hero">
    <div class="hero-photo" role="img" aria-label="Business team of four seated around a glass meeting table"></div>
    <div class="hero-ground" role="img" aria-label="Green grass hill with small trees and a house folded from banknotes"></div>
    <h1 class="hero-title">Lorem ipsum is simply<br>dummy text for web.</h1>
    <div class="hero-copy">
      <p>Pellentesque habitant morbi tristique <b>malesuada fames</b><br>ac turpis egestas. Vestibulum tortor quam, feugiat vitae,<br>ultricies eget,</p>
      <p>tempor sit amet, ante. Donec eu <b>libero sit amet</b> quam egestas<br>semper. Aenean ultricies mi vitae est.</p>
    </div>
    <a class="btn btn-start">START NOW
      <svg width="22" height="22" viewBox="0 0 22 22"><circle cx="11" cy="11" r="10" fill="#fff"/><path d="M9 6l6 5-6 5z" fill="#7d7a12"/></svg></a>
    <div class="slider-dots"><i class="on"></i><i></i><i></i></div>
  </section>

  <section class="features">
    <article class="feature">
      <div class="feature-head">
        <svg width="64" height="46" viewBox="0 0 64 46"><rect x="4" y="8" width="34" height="22" rx="3" fill="#6fae3a" transform="rotate(-12 20 20)"/><rect x="18" y="16" width="40" height="26" rx="4" fill="#b8632a"/><circle cx="22" cy="38" r="7" fill="#e2b71e"/></svg>
        <span class="feature-title">Lorem ipsum doler</span></div>
      <p>When you call The Clearpath<br>Relief Group, we will advise you<br>on the all of the possible<br>options to obtain relief...</p>
      <a class="btn btn-more">read more <svg width="15" height="15" viewBox="0 0 22 22"><circle cx="11" cy="11" r="10" fill="#fff"/><path d="M9 6l6 5-6 5z" fill="#7d7a12"/></svg></a>
    </article>
    <article class="feature">
      <div class="feature-head">
        <svg width="48" height="46" viewBox="0 0 48 46"><path d="M4 22L24 4l20 18" fill="none" stroke="#a3401c" stroke-width="5"/><rect x="10" y="20" width="28" height="22" fill="#f0d79a"/><rect x="20" y="28" width="8" height="14" fill="#c0392b"/></svg>
        <span class="feature-title">Lorem ipsum doler</span></div>
      <p>What if lower mortgage rates<br>meant you could finally afford<br>your payments? Prevent and<br>protect yourself from<br>foreclosure...</p>
      <a class="btn btn-more">read more <svg width="15" height="15" viewBox="0 0 22 22"><circle cx="11" cy="11" r="10" fill="#fff"/><path d="M9 6l6 5-6 5z" fill="#7d7a12"/></svg></a>
    </article>
    <article class="feature">
      <div class="feature-head">
        <svg width="48" height="46" viewBox="0 0 48 46"><path d="M6 4h26l10 10v30H6z" fill="#f2f2f2" stroke="#ccc"/><text x="10" y="36" font-family="Arimo, sans-serif" font-weight="700" font-size="24" fill="#1f6fa8">%</text></svg>
        <span class="feature-title">Lorem ipsum doler</span></div>
      <p>Have you had run-ins with the<br>IRS? Are you late filing your<br>returns? Do you owe more<br>than you can pay? Protect<br>yourself...</p>
      <a class="btn btn-more">read more <svg width="15" height="15" viewBox="0 0 22 22"><circle cx="11" cy="11" r="10" fill="#fff"/><path d="M9 6l6 5-6 5z" fill="#7d7a12"/></svg></a>
    </article>
    <article class="feature">
      <div class="feature-head">
        <svg width="44" height="46" viewBox="0 0 44 46"><circle cx="22" cy="23" r="15" fill="none" stroke="#e8e8e8" stroke-width="9"/><circle cx="22" cy="23" r="15" fill="none" stroke="#e0521c" stroke-width="9" stroke-dasharray="12 11.5"/></svg>
        <span class="feature-title">Lorem ipsum doler</span></div>
      <p>Out of Time and Options?<br>Bankruptcy may be the only<br>way to protect yourself and<br>your assets from creditors...</p>
      <a class="btn btn-more">read more <svg width="15" height="15" viewBox="0 0 22 22"><circle cx="11" cy="11" r="10" fill="#fff"/><path d="M9 6l6 5-6 5z" fill="#7d7a12"/></svg></a>
    </article>
  </section>
</body>
</html>
```